依頼概要
■依頼の目的/概要
飲み屋や美容室、その他色々な所に貼るポスターやフライヤーのポップのデザイン。
ターゲットは20代から50代までの富裕層。
店のイメージカラーは白、紺、グレー。
通りがかりの人に目を引くようなデザインでお願いします。
毎月のキャンペーンコースが変えられるようなスペースをお願いします。
メニューはボディー、フェイシャル、脱毛のトータルケアサロンです。
怪しいお店と勘違いされるので、清潔感のあるイメージでおねがいします。
依頼公開後の追記内容
出来ればアジアン風にしていただけると助かります。
店のイメージカラー以外の色を全然使っていただいて構いませんので。
こちらがメンズのお店のロゴです!
こちらがレディースで使用しているロゴになります。
レディースの方は宣伝程度でお洒落にロゴを貼り付ける程度でお願いします。
メンズはハワイやバリなどのイメージで。レディースはアジアンチックな感じでお願いします。
人物画などは欲しいとゆうこだわりはそこまでございませんが、雰囲気などでインパクトを与えられたらなと思います。風景などに使う色も全然派手めな感じでも構いません。
ロゴがあまりにも目立たなくならなければ何も問題はありませんのでよろしくお願いします。
些細な質問でも構いませんのでお待ちしております。
もう少し延期させていただきます。

```html
<!DOCTYPE html>
<html lang="ja">
<head>
<meta charset="utf-8">
<title>nalu men tahitian spa</title>
<link rel="stylesheet" href="https://fonts.googleapis.com/css2?family=Shippori+Mincho+B1:wght@500;700;800&family=Quicksand:wght@400;500&display=swap">
<style>
  :root {
    --paper: #ffffff;
    --teal: #1f6f6b;
    --teal-deep: #15534f;
    --teal-soft: #2c8580;
    --ink: #1d3a44;
    --ink-soft: #4a5a60;
    --flower: #5b4a8c;
    --leaf: #2f6b3a;
    --skin: #c9a58a;
    --salon: #b8896b;
  }
  * { margin: 0; padding: 0; box-sizing: border-box; }
  html, body { width: 849px; height: 1200px; overflow: hidden; background: var(--paper); }
  .poster {
    position: relative; width: 849px; height: 1200px; overflow: hidden;
    background: var(--paper);
    font-family: "Shippori Mincho B1", serif; color: var(--ink);
  }
  .corner-art { position: absolute; }
  .corner-art--flowers { left: 0; top: 0; width: 190px; height: 150px;
    background: radial-gradient(ellipse at 30% 35%, #6d5ca0 0%, #8577b3 45%, rgba(255,255,255,0) 72%); }
  .corner-art--leaves { right: 0; top: 330px; width: 200px; height: 120px;
    background: radial-gradient(ellipse at 65% 50%, #3d7d47 0%, #5e9a66 45%, rgba(255,255,255,0) 72%); }
  .brand { position: absolute; left: 0; right: 0; top: 80px; text-align: center; font-family: "Quicksand", sans-serif; color: var(--ink-soft); }
  .brand__mark { width: 150px; height: 150px; margin: 0 auto 26px; border: 3px solid var(--flower); border-radius: 50%; }
  .brand__name { font-size: 64px; font-weight: 400; letter-spacing: 1px; line-height: 1; }
  .brand__tag { font-size: 20px; margin-top: 10px; letter-spacing: 2px; }
  .feature { position: absolute; left: 0; top: 396px; width: 849px; height: 804px;
    background: linear-gradient(180deg, var(--teal-soft) 0%, var(--teal) 40%, var(--teal-deep) 100%); }
  .headline { position: absolute; left: 120px; top: 12px; color: var(--paper); font-weight: 800; font-size: 44px; line-height: 1.4; letter-spacing: 2px; }
  .headline__line { display: block; }
  .headline__line--second { margin-left: 78px; }
  .course { position: absolute; background: var(--paper); padding: 20px 24px; }
  .course__title { font-size: 38px; font-weight: 800; color: var(--ink); letter-spacing: 1px; }
  .course__title .star { color: var(--teal); margin-right: 6px; }
  .course__text { font-size: 14px; line-height: 1.6; color: var(--ink-soft); margin-top: 8px; }
  .course__price { position: absolute; font-size: 34px; font-weight: 700; color: var(--ink); }
  .course__price small { font-size: 22px; }
  .course--facial { left: 28px; top: 156px; width: 793px; height: 198px; }
  .course--facial .course__text { width: 470px; }
  .course--facial .course__price { left: 200px; bottom: 14px; }
  .course__photo { position: absolute; right: 14px; top: 14px; width: 270px; height: 158px;
    background: linear-gradient(135deg, #e8d6c4 0%, var(--skin) 55%, #8c6b55 100%); }
  .course--hair { left: 28px; top: 396px; width: 391px; height: 198px; }
  .course--body { left: 430px; top: 396px; width: 391px; height: 198px; }
  .course--hair .course__price, .course--body .course__price { right: 24px; bottom: 16px; }
  .campaign { position: absolute; left: 28px; top: 617px; width: 306px; height: 170px; background: var(--paper); padding: 16px 18px; }
  .campaign__title { font-size: 30px; font-weight: 800; padding-bottom: 8px; border-bottom: 2px solid var(--teal); }
  .campaign__text { font-size: 18px; font-weight: 700; line-height: 1.75; margin-top: 12px; }
  .salon-ad { position: absolute; left: 345px; top: 617px; width: 476px; height: 170px;
    background: linear-gradient(120deg, #d9b89c 0%, var(--salon) 50%, #7a4f3a 100%); }
  .salon-ad__label { position: absolute; right: 60px; top: 40px; width: 180px; text-align: center; color: var(--paper); font-family: "Quicksand", sans-serif; }
  .salon-ad__label span { display: block; font-size: 13px; letter-spacing: 1px; }
  .salon-ad__label strong { display: block; font-size: 30px; font-weight: 500; line-height: 1.2; }
</style>
</head>
<body>
<div class="poster">
  <div class="corner-art corner-art--flowers" role="img" aria-label="Purple tropical flowers with green leaves"></div>
  <div class="corner-art corner-art--leaves" role="img" aria-label="Green tropical leaves"></div>

  <header class="brand">
    <div class="brand__mark"></div>
    <div class="brand__name">nalu men</div>
    <div class="brand__tag">✲ tahitian spa ✲</div>
  </header>

  <section class="feature" role="img" aria-label="Teal panel with an ornamental damask pattern">
    <h1 class="headline"><span class="headline__line">こだわりの技術で</span><span class="headline__line headline__line--second">ワンランク上の男に</span></h1>

    <article class="course course--facial">
      <h2 class="course__title"><span class="star">✲</span>フェイシャルコース</h2>
      <p class="course__text">マッサージで老廃物の排出を促し、すっきり整えた肌へ。<br>ハリとツヤのあるフェイスラインを目指します。</p>
      <p class="course__price">10,000<small>円</small></p>
      <div class="course__photo" role="img" aria-label="Photo of a man receiving a facial treatment"></div>
    </article>

    <article class="course course--hair">
      <h2 class="course__title"><span class="star">✲</span>脱毛コース</h2>
      <p class="course__text">お悩みのムダ毛をスペシャリストが丁寧にケアします。</p>
      <p class="course__price">10,000<small>円～</small></p>
    </article>

    <article class="course course--body">
      <h2 class="course__title"><span class="star">✲</span>ボディコース</h2>
      <p class="course__text">全身の凝りを丁寧にほぐすトリートメントで、疲れにくい体へと導きます。</p>
      <p class="course__price">20,000<small>円</small></p>
    </article>

    <aside class="campaign">
      <h2 class="campaign__title">今月のキャンペーン</h2>
      <p class="campaign__text">今月限定で○○○を00％OFF！<br>この機会に是非お試しください。</p>
    </aside>

    <aside class="salon-ad" role="img" aria-label="Photo of a woman relaxing in a spa with flower petals">
      <div class="salon-ad__label">
        <span>ladies salon</span>
        <strong>nalu nani</strong>
        <span>tahitian spa</span>
      </div>
    </aside>
  </section>
</div>
</body>
</html>
```